Business card design needed

Double sided
Color, unique, elegant

Maybe put this quote somewhere?? But I think it might make it to cluttered?
“The Pilates Method of Body
Conditioning develops the body
uniformly, corrects posture, restores
vitality, invigorates the mind and
elevates the spirit”
- Henrik Dovacombe

Industry/Entity Type

Business

Contact Information for Business Card

Marta Kellbrook
Pilates Instructor & Personal trainer
Mobile: 0498265043
www.lorvix.com.au
email: lorvixhealth.fitness@qentamail.com

```html
<!DOCTYPE html>
<html lang="en">
<head>
<meta charset="utf-8">
<title>Lorvix Health and Fitness – Business Card</title>
<link href="https://fonts.googleapis.com/css2?family=Questrial&display=swap" rel="stylesheet">
<style>
  :root {
    --backdrop: #2b2b2b;
    --card-green: #86c97b;
    --card-white: #f7f7f7;
    --ink-black: #0c0c0c;
    --ink-dark: #2f3a2c;
    --ink-text: #1c1c1c;
    --accent-pink: #b56bb4;
    --quote-white: #f2f8ef;
    --card-w: 560px;
    --card-h: 320px;
  }
  * { box-sizing: border-box; margin: 0; padding: 0; }
  html, body {
    width: 1200px; height: 900px; overflow: hidden;
    background: var(--backdrop);
    font-family: "Questrial", "Century Gothic", sans-serif;
  }
  .stage {
    width: 1200px; height: 900px;
    display: flex; flex-direction: column;
    align-items: center; justify-content: center; gap: 60px;
  }
  .card {
    position: relative;
    width: var(--card-w); height: var(--card-h);
    overflow: hidden;
  }
  .card-art { position: absolute; inset: 0; width: 100%; height: 100%; }

  /* Front */
  .card-front { background: var(--card-green); }
  .front-copy {
    position: absolute; left: 40px; top: 130px; width: 290px;
    display: flex; flex-direction: column;
  }
  .brand { color: var(--ink-dark); }
  .brand-name {
    font-size: 54px; letter-spacing: 6px; line-height: 1;
    font-weight: 400; text-transform: uppercase;
  }
  .brand-tagline { font-size: 21px; line-height: 1.2; margin-top: 4px; letter-spacing: 0.5px; }
  .quote {
    align-self: center; width: 220px; margin-top: 14px;
    color: var(--quote-white); font-size: 11px; line-height: 1.4;
    text-align: center;
  }
  .quote cite { display: block; font-style: normal; }

  /* Back */
  .card-back { background: var(--card-white); }
  .person { position: absolute; left: 34px; top: 138px; }
  .person-name { font-size: 16px; font-weight: 400; color: var(--ink-text); }
  .person-role {
    font-size: 11px; color: var(--accent-pink);
    letter-spacing: 0.8px; text-transform: uppercase; margin-top: 2px;
  }
  .person-marker {
    position: absolute; left: 0; top: 140px;
    width: 0; height: 0;
    border-top: 9px solid transparent; border-bottom: 9px solid transparent;
    border-left: 12px solid var(--accent-pink);
  }
  .contacts {
    position: absolute; left: 34px; top: 218px;
    list-style: none; display: flex; flex-direction: column; gap: 9px;
  }
  .contact { display: flex; align-items: center; gap: 12px; font-size: 15px; color: var(--ink-text); white-space: nowrap; }
  .contact-icon { width: 20px; height: 20px; flex: none; }
</style>
</head>
<body>
<main class="stage">

  <section class="card card-front" aria-label="Card front">
    <svg class="card-art" viewBox="0 0 560 320" aria-hidden="true">
      <path d="M300 0 H560 V150 C520 205 440 215 380 190 C320 165 290 110 295 60 C297 35 300 15 300 0 Z" fill="var(--ink-black)"/>
    </svg>
    <svg class="card-art" viewBox="0 0 560 320" role="img" aria-label="Pink silhouette of a woman in a Pilates stretch with a flowing ribbon">
      <defs>
        <linearGradient id="figureFront" x1="0" y1="0" x2="1" y2="1">
          <stop offset="0" stop-color="#c27ac0"/>
          <stop offset="1" stop-color="#9a5a99"/>
        </linearGradient>
      </defs>
      <ellipse cx="420" cy="100" rx="70" ry="50" fill="url(#figureFront)" opacity="0.85"/>
    </svg>
    <div class="front-copy">
      <div class="brand">
        <h1 class="brand-name">Lorvix</h1>
        <p class="brand-tagline">Health and Fitness</p>
      </div>
      <blockquote class="quote">
        “The Pilates Method of Body Conditioning develops the body uniformly, corrects posture, restores vitality, invigorates the mind and elevates the spirit”
        <cite>- Henrik Dovacombe</cite>
      </blockquote>
    </div>
  </section>

  <section class="card card-back" aria-label="Card back">
    <svg class="card-art" viewBox="0 0 560 320" aria-hidden="true">
      <path d="M330 0 H560 V320 H535 C420 300 335 210 325 120 C320 70 322 30 330 0 Z" fill="var(--ink-black)"/>
    </svg>
    <svg class="card-art" viewBox="0 0 560 320" role="img" aria-label="Pink silhouette of a woman reaching upward in a Pilates stretch with a flowing ribbon">
      <defs>
        <linearGradient id="figureBack" x1="0" y1="0" x2="0" y2="1">
          <stop offset="0" stop-color="#c27ac0"/>
          <stop offset="1" stop-color="#9a5a99"/>
        </linearGradient>
      </defs>
      <ellipse cx="440" cy="150" rx="60" ry="115" fill="url(#figureBack)" opacity="0.85"/>
    </svg>
    <span class="person-marker" aria-hidden="true"></span>
    <div class="person">
      <h2 class="person-name">Marta Kellbrook</h2>
      <p class="person-role">Pilates Instructor &amp; Personal Trainer</p>
    </div>
    <ul class="contacts">
      <li class="contact">
        <svg class="contact-icon" viewBox="0 0 20 20" aria-hidden="true"><circle cx="10" cy="10" r="10" fill="var(--accent-pink)"/><path d="M7 5.5 L8.6 5.5 L9.3 7.8 L8.3 8.7 C8.9 10 10 11.1 11.3 11.7 L12.2 10.7 L14.5 11.4 L14.5 13 C14.5 13.6 14 14 13.4 14 C9.6 13.8 6.2 10.4 6 6.6 C6 6 6.4 5.5 7 5.5 Z" fill="#fff"/></svg>
        <span>0498265043</span>
      </li>
      <li class="contact">
        <svg class="contact-icon" viewBox="0 0 20 20" aria-hidden="true"><circle cx="10" cy="10" r="10" fill="var(--accent-pink)"/><rect x="5" y="6.5" width="10" height="7" rx="1" fill="#fff"/><path d="M5.5 7 L10 10.5 L14.5 7" fill="none" stroke="var(--accent-pink)" stroke-width="1"/></svg>
        <span>lorvixhealth.fitness@qentamail.com</span>
      </li>
      <li class="contact">
        <svg class="contact-icon" viewBox="0 0 20 20" aria-hidden="true"><circle cx="10" cy="10" r="10" fill="var(--accent-pink)"/><path d="M10 4.5 C7.8 4.5 6.3 6.1 6.3 8.1 C6.3 10.8 10 15 10 15 C10 15 13.7 10.8 13.7 8.1 C13.7 6.1 12.2 4.5 10 4.5 Z" fill="#fff"/><circle cx="10" cy="8.2" r="1.4" fill="var(--accent-pink)"/></svg>
        <span>www.lorvix.com.au</span>
      </li>
    </ul>
  </section>

</main>
</body>
</html>
```